MR Business Card

I want to create a simple business card.
I am a consultant. I design and develop furniture, lighting and accessories for hospitality and retail brands.
I want the card to be simple and clean. Not too much of a logo - but it needs the basic information shown on the attached file.
Also - I have shown some fonts that I like on the attached file.
The card can be square or rectangle. It should be double sided.
I prefer 1-2 colors (not too colorful - but using color an an accent) Even if using color on the edges as an accent.

My snapgrove link shows some other graphics styles that I like. I like clean and simple.
http://www.snapgrove-boards.net/marenrosko/business-cards/

```html
<!DOCTYPE html>
<html lang="en">
<head>
<meta charset="utf-8">
<title>Maren Rosko — Business Card</title>
<link rel="stylesheet" href="https://fonts.googleapis.com/css2?family=Josefin+Sans:wght@300;400;600&display=swap">
<style>
  :root {
    --canvas: #ecebe8;
    --card: #fbfbfa;
    --accent-light: #cfe7ee;
    --accent: #5f94a2;
    --accent-soft: #8fc3d0;
    --rule: #e2e4e4;
    --shadow: rgba(0, 0, 0, 0.12);
  }
  * { box-sizing: border-box; margin: 0; padding: 0; }
  html, body {
    width: 1200px;
    height: 900px;
    overflow: hidden;
    background: var(--canvas);
    font-family: "Josefin Sans", sans-serif;
  }
  .sheet {
    width: 1200px;
    height: 900px;
    display: flex;
    flex-direction: column;
    align-items: center;
    justify-content: center;
    gap: 56px;
  }
  .card {
    position: relative;
    width: 630px;
    height: 360px;
    background: var(--card);
    box-shadow: 0 6px 18px var(--shadow);
    overflow: hidden;
  }

  /* Back side: name and contact band */
  .card-back .band {
    position: absolute;
    left: 0;
    right: 0;
    top: 118px;
    height: 124px;
    border-top: 1px solid var(--rule);
    border-bottom: 1px solid var(--rule);
    display: flex;
  }
  .identity {
    width: 318px;
    padding: 34px 26px 0 0;
    text-align: right;
    border-right: 1px solid var(--rule);
  }
  .identity .name {
    font-weight: 400;
    font-size: 31px;
    letter-spacing: 1px;
    color: var(--accent);
    text-transform: uppercase;
    line-height: 1;
  }
  .identity .trade {
    margin-top: 10px;
    font-weight: 300;
    font-size: 15px;
    letter-spacing: 2.5px;
    color: var(--accent);
    text-transform: uppercase;
  }
  .identity .amp { color: var(--accent-soft); }
  .contact {
    padding: 22px 0 0 24px;
    color: var(--accent-soft);
  }
  .contact .phone {
    font-weight: 400;
    font-size: 25px;
    letter-spacing: 1.5px;
    line-height: 1;
  }
  .contact .email {
    margin-top: 10px;
    font-weight: 400;
    font-size: 14px;
    letter-spacing: 1.5px;
    text-transform: uppercase;
  }

  /* Front side: diagonal accent and monogram */
  .card-front .diagonal {
    position: absolute;
    inset: 0;
    width: 100%;
    height: 100%;
  }
  .monogram {
    position: absolute;
    left: 50%;
    top: 50%;
    transform: translate(-50%, -50%);
    display: flex;
    align-items: center;
    gap: 10px;
    font-weight: 600;
    font-size: 64px;
    letter-spacing: 2px;
    color: var(--accent);
    line-height: 1;
  }
  .monogram .mark-square {
    width: 14px;
    height: 14px;
    background: var(--accent);
  }
</style>
</head>
<body>
  <main class="sheet">
    <section class="card card-back" aria-label="Card back">
      <div class="band">
        <div class="identity">
          <p class="name">Maren Rosko</p>
          <p class="trade">Hospitality <span class="amp">&amp;</span> Home</p>
        </div>
        <div class="contact">
          <p class="phone">555.014.2287</p>
          <p class="email">maren@marenrosko.com</p>
        </div>
      </div>
    </section>

    <section class="card card-front" aria-label="Card front">
      <svg class="diagonal" viewBox="0 0 630 360" preserveAspectRatio="none" aria-hidden="true">
        <polygon points="0,0 630,0 0,350" fill="var(--accent-light)"/>
      </svg>
      <div class="monogram">
        <span class="mark-square"></span>
        <span class="initials">MR</span>
      </div>
    </section>
  </main>
</body>
</html>
```